Physiotherapy business needs patient information graphic redesign

We have existing graphics that we need redesigned to add some artistic flare. The images must remain professional and suitable for a healthcare setting but some artistic flare is need to add interest to the graphics so that patients are able to engage more easily with the info sheet. Graphics include "INS", "graded activity", "pacing I", "pacing II" and "sleep"

Target Market(s)

Practitioners and patients with pain

Industry/Entity Type

Business

Font styles to use
Sans Serif

Colors
3176b5
9bcb3b
ec1f27

Requirements
Must have
• The ability to communicate the message in the graphic
• Artistic flair
• Retain professionalism
Nice to have
• Unique creativity that distinguishes our product
• Matching with our logo (attached). Does not have to be the same colours or style/font but still should fit with the logo stylistically
Should not have
• A similar boring and flat feel as the existing graphics

```html
<!DOCTYPE html>
<html lang="en">
<head>
<meta charset="utf-8">
<title>Pain Cycle</title>
<link rel="stylesheet" href="https://fonts.googleapis.com/css2?family=Open+Sans:wght@600;700;800&display=swap">
<style>
  :root {
    --blue: #3176b5;
    --blue-light: #4f95d3;
    --green: #9bcb3b;
    --green-light: #b6de62;
    --red: #ec1f27;
    --white: #ffffff;
  }
  html, body {
    margin: 0;
    padding: 0;
    width: 1200px;
    height: 1200px;
    overflow: hidden;
    background: var(--white);
  }
  .cycle-graphic {
    display: block;
    width: 1200px;
    height: 1200px;
  }
  .segment--blue { fill: url(#blueSweep); }
  .segment--green { fill: url(#greenSweep); }
  .segment-sheen { fill: url(#sheen); }
  .badge-ring { fill: url(#badgeRing); }
  .badge-core { fill: url(#badgeCore); }
  .icon-accent { fill: var(--red); }
  .icon-blue { fill: var(--blue); }
  .icon-green { fill: var(--green); }
  .icon-crack {
    fill: none;
    stroke: var(--white);
    stroke-width: 6;
    stroke-linejoin: round;
    stroke-linecap: round;
  }
  .icon-battery-shell {
    fill: none;
    stroke: var(--blue);
    stroke-width: 8;
  }
  .icon-glyph {
    font-family: "Open Sans", Arial, sans-serif;
    font-weight: 800;
    fill: var(--green);
    text-anchor: middle;
  }
  .icon-glyph--accent { fill: var(--red); }
  .stage-label {
    font-family: "Open Sans", Arial, sans-serif;
    font-weight: 600;
    font-size: 34px;
    fill: var(--white);
    text-anchor: middle;
    letter-spacing: 0.3px;
  }
  .hub-title {
    font-family: "Open Sans", Arial, sans-serif;
    font-weight: 700;
    font-size: 96px;
    fill: var(--blue);
    text-anchor: middle;
    letter-spacing: 2px;
  }
</style>
</head>
<body>
<svg class="cycle-graphic" viewBox="0 0 1500 1500" xmlns="http://www.w3.org/2000/svg" role="img" aria-label="Pain cycle: increased pain, anxiety and depression, disrupted sleep, mood instability and decreased coping ability">
  <defs>
    <linearGradient id="blueSweep" x1="0" y1="0" x2="1" y2="1">
      <stop offset="0%" stop-color="#4f95d3"/>
      <stop offset="100%" stop-color="#2a66a0"/>
    </linearGradient>
    <linearGradient id="greenSweep" x1="0" y1="0" x2="1" y2="1">
      <stop offset="0%" stop-color="#b6de62"/>
      <stop offset="100%" stop-color="#86b52c"/>
    </linearGradient>
    <radialGradient id="sheen" cx="35%" cy="25%" r="70%">
      <stop offset="0%" stop-color="#ffffff" stop-opacity="0.22"/>
      <stop offset="100%" stop-color="#ffffff" stop-opacity="0"/>
    </radialGradient>
    <radialGradient id="badgeRing" cx="50%" cy="45%" r="55%">
      <stop offset="70%" stop-color="#ffffff"/>
      <stop offset="100%" stop-color="#e3e8ee"/>
    </radialGradient>
    <radialGradient id="badgeCore" cx="40%" cy="35%" r="70%">
      <stop offset="0%" stop-color="#e6eaef"/>
      <stop offset="60%" stop-color="#f3f5f7"/>
      <stop offset="100%" stop-color="#ffffff"/>
    </radialGradient>
    <filter id="softLift" x="-20%" y="-20%" width="140%" height="140%">
      <feDropShadow dx="0" dy="10" stdDeviation="14" flood-color="#1c3550" flood-opacity="0.22"/>
    </filter>
    <filter id="badgeLift" x="-30%" y="-30%" width="160%" height="160%">
      <feDropShadow dx="0" dy="6" stdDeviation="8" flood-color="#1c3550" flood-opacity="0.25"/>
    </filter>
  </defs>

  <g class="cycle-segments" filter="url(#softLift)">
    <path class="segment segment--blue" d="M289.9,629.4 A495,495 0 0 1 770,255 A155,155 0 0 1 770,565 A185,185 0 0 0 600,677.1 A185,185 0 0 0 289.9,629.4 Z"/>
    <path class="segment segment--green" d="M890.6,269.9 A495,495 0 0 1 1265,750 A155,155 0 0 1 955,750 A185,185 0 0 0 842.9,580 A185,185 0 0 0 890.6,269.9 Z"/>
    <path class="segment segment--blue" d="M1250.1,870.6 A495,495 0 0 1 770,1245 A155,155 0 0 1 770,935 A185,185 0 0 0 940,822.9 A185,185 0 0 0 1250.1,870.6 Z"/>
    <path class="segment segment--green" d="M649.4,1230.1 A495,495 0 0 1 275,750 A155,155 0 0 1 585,750 A185,185 0 0 0 697.1,920 A185,185 0 0 0 649.4,1230.1 Z"/>
  </g>
  <g class="cycle-sheen">
    <path class="segment-sheen" d="M289.9,629.4 A495,495 0 0 1 770,255 A155,155 0 0 1 770,565 A185,185 0 0 0 600,677.1 A185,185 0 0 0 289.9,629.4 Z"/>
    <path class="segment-sheen" d="M890.6,269.9 A495,495 0 0 1 1265,750 A155,155 0 0 1 955,750 A185,185 0 0 0 842.9,580 A185,185 0 0 0 890.6,269.9 Z"/>
    <path class="segment-sheen" d="M1250.1,870.6 A495,495 0 0 1 770,1245 A155,155 0 0 1 770,935 A185,185 0 0 0 940,822.9 A185,185 0 0 0 1250.1,870.6 Z"/>
    <path class="segment-sheen" d="M649.4,1230.1 A495,495 0 0 1 275,750 A155,155 0 0 1 585,750 A185,185 0 0 0 697.1,920 A185,185 0 0 0 649.4,1230.1 Z"/>
  </g>

  <!-- increased pain -->
  <g class="badge badge--increased-pain" filter="url(#badgeLift)">
    <circle class="badge-ring" cx="770" cy="410" r="122"/>
    <circle class="badge-core" cx="770" cy="410" r="96"/>
  </g>
  <g class="icon icon--bolt" role="img" aria-label="Lightning bolt">
    <path class="icon-accent" d="M786,348 L738,420 L766,420 L750,474 L804,394 L776,394 L796,348 Z"/>
  </g>

  <!-- anxiety & depression -->
  <g class="badge badge--anxiety" filter="url(#badgeLift)">
    <circle class="badge-ring" cx="1105" cy="750" r="122"/>
    <circle class="badge-core" cx="1105" cy="750" r="96"/>
  </g>
  <g class="icon icon--broken-heart" role="img" aria-label="Broken heart">
    <path class="icon-accent" d="M1105,805 C1035,758 1040,700 1077,700 C1092,700 1101,709 1105,718 C1109,709 1118,700 1133,700 C1170,700 1175,758 1105,805 Z"/>
    <polyline class="icon-crack" points="1105,716 1094,744 1114,758 1100,795"/>
  </g>

  <!-- disrupted sleep -->
  <g class="badge badge--sleep" filter="url(#badgeLift)">
    <circle class="badge-ring" cx="770" cy="1095" r="122"/>
    <circle class="badge-core" cx="770" cy="1095" r="96"/>
  </g>
  <g class="icon icon--battery" role="img" aria-label="Low battery">
    <rect class="icon-blue" x="757" y="1030" width="26" height="12" rx="3"/>
    <rect class="icon-battery-shell" x="744" y="1042" width="52" height="100" rx="9"/>
    <rect class="icon-accent" x="755" y="1118" width="30" height="14" rx="3"/>
  </g>

  <!-- mood instability -->
  <g class="badge badge--mood" filter="url(#badgeLift)">
    <circle class="badge-ring" cx="420" cy="750" r="122"/>
    <circle class="badge-core" cx="420" cy="750" r="96"/>
  </g>
  <g class="icon icon--questions" role="img" aria-label="Question and exclamation marks">
    <text class="icon-glyph" x="392" y="748" font-size="64">?</text>
    <text class="icon-glyph icon-glyph--accent" x="424" y="735" font-size="54">!</text>
    <text class="icon-glyph" x="452" y="756" font-size="72">?</text>
    <text class="icon-glyph" x="410" y="800" font-size="50">?</text>
    <text class="icon-glyph icon-glyph--accent" x="440" y="802" font-size="44">!</text>
  </g>

  <!-- stage labels -->
  <text class="stage-label" x="535" y="472">INCREASED</text>
  <text class="stage-label" x="535" y="516">PAIN</text>

  <text class="stage-label" x="1070" y="525">ANXIETY &amp;</text>
  <text class="stage-label" x="1070" y="569">DEPRESSION</text>

  <text class="stage-label" x="1002" y="1024">DISRUPTED</text>
  <text class="stage-label" x="1002" y="1068">SLEEP</text>

  <text class="stage-label" x="472" y="927">MOOD INSTABILITY</text>
  <text class="stage-label" x="472" y="968">&amp; DECREASED</text>
  <text class="stage-label" x="472" y="1009">COPING</text>
  <text class="stage-label" x="472" y="1050">ABILITY</text>

  <!-- hub -->
  <text class="hub-title" x="766" y="786">PAIN</text>
</svg>
</body>
</html>
```